Ridgecrest Capital Allies need a desert themed website!

We need a web design and development for our informational website for our new company named Ridgecrest Capital Allies. We would like it to be desert themed and it can be color or black and white. We would like it to be classy and clean, while also talking to the benefits of investment partner with us.

We're thinking probably a home page with a nice image of a Scottsdale landscape, then other pages would What we offer our partners page (or other wording if you find something better), a meet the founder page, and a contact us page.

What we offer our partners (or other wording if you think of something better):
Our investors offer an opportunity to families that cannot usually get approved for a mortgage, to be able to become future homeowners. Thus, Benefiting both the investors and local surrounding community members. Our investors get to both have all the benefits of an investment with receiving above market rates of return to themselves and helping families find homes at the same time.

Maybe also build an infographic with these benefits: Safety, Security, Long-term investment horizon, cashflow, tax benefits, above market rate of return, and capital growth.

And a meet the founder page. With my headshot.

Paul Harnetti is a private equity investor providing significantly above market returns to his investment partners while taking the time to be involved with his community and family. Paul first honed his skills in taking calculated risk decisions while very young where he took on playing poker professionally. He succeeded at the highest levels for over a decade competing in high stakes professional cash games around the world.

From the poker world he transitioned to investing in public and private markets. He took an approach of knowing the companies he invests in intimately and after over 10,000 hours of research became known in his community as the person to get investment advice on the electric vehicle industry for his voracious research and expert insight.

He now invests in single family homes in the Phoenix market using his past experience analyzing probabilistic outcomes and comparing the ROIs of different potential strategies. These skills have contributed to his success in investing in companies where he used his ability to assess risk to reward ratios to significantly outperform the market over an extended period.

Contact page we want my email Paul@RidgecrestFunds.example, my instagram: @PaulHarnetti, and my linkedin https://www.profilehub.example/in/paul-harnetti-58172036/

I have included my headshot for the about me page. I've included some saguaro generated images feel free to incorporate into the website (or make them the company logo), or not, whatever you feel gives the best look for the website.

```html
<!DOCTYPE html>
<html lang="en">
<head>
<meta charset="utf-8">
<title>Ridgecrest Capital Allies</title>
<link href="https://fonts.googleapis.com/css2?family=Oswald:wght@500;600&family=Poppins:wght@400;500;600&display=swap" rel="stylesheet">
<style>
:root{
  --brown:#9a6530;
  --brown-dark:#6e4b25;
  --brown-bar:#8c6232;
  --heading:#8a6a3f;
  --cream:#fbf7ec;
  --ring:#f0dfb8;
  --ink:#2a2a2a;
  --field:#f2f2f2;
  --white:#ffffff;
}
*{box-sizing:border-box;margin:0;padding:0}
html,body{width:1200px;height:4754px;overflow:hidden}
body{font-family:"Poppins",sans-serif;color:var(--ink);background:var(--white);position:relative}
.section{position:absolute;left:0;width:1200px}
.abs{position:absolute}
.h-display{font-family:"Oswald",sans-serif;font-weight:600;text-transform:uppercase;color:var(--heading);letter-spacing:0.5px}
.center{text-align:center;left:0;width:1200px}
.rule{position:absolute;height:3px;width:62px;background:var(--brown)}
.btn{position:absolute;display:flex;align-items:center;justify-content:center;background:var(--brown);color:var(--white);font-size:13px;font-weight:500;border-radius:20px;height:36px}
.body-text{font-size:12.5px;line-height:23px;color:#333}

/* hero */
.hero{top:0;height:610px}
.hero-photo{position:absolute;inset:0;height:600px;background:linear-gradient(180deg,#4f93d8 0%,#a9c9e2 28%,#e9c477 48%,#c99a4f 70%,#8e6a3a 100%)}
.logo{position:absolute;display:flex;align-items:center}
.logo-mark{width:92px;height:92px;border-radius:50%;background:#e9c68a;border:4px solid var(--white)}
.logo-text{margin-left:10px}
.logo-name{font-family:"Oswald",sans-serif;font-weight:600;font-size:32px;line-height:34px;color:#1c1c1c;text-transform:uppercase}
.logo-tag{font-size:15px;color:#1c1c1c}
.nav{position:absolute;top:52px;left:568px;display:flex;gap:40px;font-size:13px;color:#1c1c1c}
.nav .active{font-weight:600}
.hero-title{font-family:"Oswald",sans-serif;font-weight:600;font-size:48px;color:#111;text-transform:uppercase}
.hero-sub{font-size:14px;font-weight:500;color:#111}

/* benefits */
.benefit{position:absolute;width:176px;height:176px;border-radius:50%;border:3px solid #8a5e2e;background:var(--white);display:flex;flex-direction:column;align-items:center;justify-content:center;text-align:center;font-size:13.5px;font-weight:500;line-height:18px}
.benefit::before{content:"";position:absolute;inset:12px;border-radius:50%;box-shadow:0 2px 10px rgba(0,0,0,0.12);z-index:0}
.benefit svg,.benefit span{position:relative;z-index:1}
.benefit svg{margin-bottom:8px}

/* testimonials */
.card{position:absolute;top:3460px;width:446px;height:222px;background:var(--white);box-shadow:0 3px 14px rgba(0,0,0,0.12);text-align:center;border-bottom:3px solid #c9b79c}
.card .stars{color:#f2a81d;font-size:18px;letter-spacing:2px;margin-top:62px}
.card p{font-size:12.5px;line-height:22px;padding:10px 14px 0}
.card .who{font-size:14px;font-weight:500;margin-top:10px}
.quote{position:absolute;top:26px;left:50%;transform:translateX(-50%);font-family:"Oswald",sans-serif;font-size:90px;line-height:90px;color:#e7e2da}
.arrow{position:absolute;top:3553px;width:36px;height:36px;border-radius:50%;display:flex;align-items:center;justify-content:center}

/* form */
.field{position:absolute;background:var(--field);font-size:12.5px;padding:14px 20px;height:44px}
.field-active{background:var(--white);border:2px solid var(--brown)}
.field-label{position:absolute;background:var(--brown);color:var(--white);font-size:9px;padding:2px 12px}

/* footer */
.footer{top:4380px;height:374px;background:var(--brown-dark);color:var(--white)}
.foot-item{position:absolute;display:flex;align-items:center;gap:14px;font-size:12.5px;line-height:19px}
.foot-icon{width:36px;height:36px;border-radius:50%;background:#c9a77c;display:flex;align-items:center;justify-content:center}
.foot-label{font-family:"Oswald",sans-serif;font-weight:600;font-size:14px}
.bottom-bar{position:absolute;top:325px;left:0;width:1200px;height:49px;background:var(--brown-bar);font-size:11.5px;display:flex;align-items:center;padding:0 141px;justify-content:space-between}
.socials{display:flex;gap:12px}
.social{width:26px;height:26px;border-radius:50%;border:1.5px solid var(--white)}
</style>
</head>
<body>

<!-- Hero -->
<header class="section hero">
  <div class="hero-photo" role="img" aria-label="Sunlit desert landscape with saguaro cactus and distant mountains"></div>
  <svg class="abs" style="left:0;top:500px" width="1200" height="110" viewBox="0 0 1200 110">
    <path d="M0 30 Q600 150 1200 30 L1200 110 L0 110 Z" fill="#ffffff"/>
    <path d="M0 30 Q600 150 1200 30" fill="none" stroke="#b27545" stroke-width="4"/>
  </svg>
  <div class="logo" style="left:142px;top:12px">
    <div class="logo-mark"></div>
    <div class="logo-text"><div class="logo-name">Ridgecrest</div><div class="logo-tag">Capital Allies</div></div>
  </div>
  <nav class="nav"><span class="active">Home</span><span>What We Offer</span><span>Meet The Founder</span></nav>
  <div class="btn" style="left:932px;top:43px;width:128px;background:#b06e3f">Contact Us</div>
  <div class="abs center hero-title" style="top:210px">Investing in a Brighter Future</div>
  <div class="abs center hero-sub" style="top:278px">Partnership Opportunities for a Prosperous Community</div>
  <div class="btn" style="left:537px;top:328px;width:126px;background:#b06e3f">Contact Us</div>
</header>

<!-- Welcome -->
<section class="section" style="top:640px;height:365px;background:var(--cream)">
  <div class="abs center h-display" style="top:24px;font-size:40px;line-height:50px">Welcome to<br>Ridgecrest Capital Allies</div>
  <div class="rule" style="left:569px;top:134px"></div>
  <p class="abs body-text" style="left:200px;top:155px;width:800px;text-align:center">Lorem ipsum dolor sit amet, consectetur adipiscing elit. Nunc sit amet tortor vel enim efficitur vulputate vel nec leo. Donec accumsan venenatis leo dictum vestibulum. Fusce ut feugiat mauris. Vivamus vehicula volutpat posuere. Nam at metus sed nunc bibendum mattis. Maecenas ex libero, tristique eget arcu ut.</p>
  <div class="btn" style="left:537px;top:240px;width:126px">Contact Us</div>
</section>

<!-- Homeownership -->
<section class="section" style="top:1005px;height:600px">
  <div class="abs h-display" style="left:141px;top:135px;font-size:33px;line-height:42px">Investing in Homeownership<br>for Families</div>
  <div class="abs body-text" style="left:141px;top:245px;width:415px">
    <p>Our investors offer an opportunity to families that cannot usually get approved for a mortgage, to be able to become future homeowners. Thus, Benefiting both the investors and local surrounding community members.</p>
    <p>Our investors get to both have all the benefits of an investment with receiving above market rates of return to themselves and helping families find homes at the same time.</p>
  </div>
  <div class="btn" style="left:141px;top:435px;width:127px">Read More</div>
  <div class="abs" style="left:654px;top:97px;width:405px;height:405px;border-radius:50%;background:var(--ring)"></div>
  <div class="abs" role="img" aria-label="Photo of two businessmen shaking hands" style="left:648px;top:111px;width:402px;height:402px;border-radius:50%;background:linear-gradient(135deg,#6b4a32,#2e3a55 55%,#1f2230)"></div>
</section>

<!-- Benefits -->
<section class="section" style="top:1605px;height:675px;background:var(--cream)">
  <div class="abs center h-display" style="top:72px;font-size:40px;line-height:50px">Benefits of Investing with<br>Ridgecrest Capital Allies</div>
  <div class="rule" style="left:569px;top:182px"></div>
  <svg class="abs" style="left:0;top:0" width="1200" height="675">
    <path d="M232 355 Q290 335 355 350 Q420 400 477 420 Q540 345 600 350 Q660 420 725 420 Q790 345 848 350 Q900 420 970 420 Q1010 340 1030 355" fill="none" stroke="#8a5e2e" stroke-width="1.5" stroke-dasharray="3 3"/>
  </svg>
  <div class="benefit" style="left:267px;top:227px"><svg width="48" height="48" viewBox="0 0 48 48" fill="none" stroke="#8a5e2e" stroke-width="2"><rect x="6" y="6" width="36" height="34" rx="2"/><rect x="12" y="12" width="24" height="22"/><circle cx="24" cy="23" r="5"/><path d="M12 40v4M36 40v4"/></svg><span>Security</span></div>
  <div class="benefit" style="left:512px;top:227px"><svg width="52" height="48" viewBox="0 0 52 48" fill="none" stroke="#8a5e2e" stroke-width="2"><rect x="6" y="14" width="40" height="22" rx="2"/><circle cx="26" cy="25" r="5"/><path d="M14 8a14 10 0 0 1 24 0M38 42a14 10 0 0 1-24 0"/></svg><span>Cashflow</span></div>
  <div class="benefit" style="left:760px;top:227px"><svg width="48" height="48" viewBox="0 0 48 48" fill="none" stroke="#8a5e2e" stroke-width="2"><circle cx="22" cy="28" r="14"/><circle cx="22" cy="28" r="9"/><path d="M22 23v10M19 25h5M19 31h5M34 6l8 8M35 8l1 1M41 13l1 1"/></svg><span>Above Market<br>Rate Of Return</span></div>
  <div class="benefit" style="left:144px;top:352px"><svg width="48" height="48" viewBox="0 0 48 48" fill="none" stroke="#8a5e2e" stroke-width="2"><path d="M26 4l12 5v9c0 7-5 12-12 14-7-2-12-7-12-14V9z"/><path d="M21 17l4 4 6-7"/><path d="M4 34h8l8 4h10l8-6"/></svg><span>Safety</span></div>
  <div class="benefit" style="left:389px;top:352px"><svg width="48" height="48" viewBox="0 0 48 48" fill="none" stroke="#8a5e2e" stroke-width="2"><path d="M18 10h10l-3 6c8 3 11 10 11 18H8c0-8 3-15 11-18z"/><circle cx="36" cy="34" r="8"/><path d="M36 30v4l3 2"/></svg><span>Long-term<br>Investment<br>Horizon</span></div>
  <div class="benefit" style="left:637px;top:352px"><svg width="48" height="48" viewBox="0 0 48 48" fill="none" stroke="#8a5e2e" stroke-width="2"><path d="M8 4h24l6 6v32H8z"/><text x="11" y="16" font-size="9" fill="#8a5e2e" stroke="none" font-family="Poppins">TAX</text><rect x="22" y="22" width="18" height="20"/><path d="M26 28h10M26 33h10M26 38h10M12 24h6M12 30h6"/></svg><span>Tax Benefits</span></div>
  <div class="benefit" style="left:882px;top:352px"><svg width="48" height="48" viewBox="0 0 48 48" fill="none" stroke="#8a5e2e" stroke-width="2"><path d="M18 4l-7 8h4v8h6v-8h4z"/><rect x="8" y="24" width="18" height="5"/><rect x="8" y="30" width="18" height="5"/><rect x="8" y="36" width="18" height="5"/><circle cx="34" cy="34" r="8"/><path d="M34 30v8"/></svg><span>Capital Growth</span></div>
  <div class="btn" style="left:537px;top:560px;width:126px">Contact Us</div>
</section>

<!-- Founder -->
<section class="section" style="top:2280px;height:590px">
  <div class="abs" style="left:141px;top:85px;width:405px;height:405px;border-radius:50%;background:var(--ring)"></div>
  <div class="abs" role="img" aria-label="Headshot portrait of founder Paul Harnetti" style="left:147px;top:100px;width:402px;height:402px;border-radius:50%;background:linear-gradient(160deg,#8c8a85,#5e5b57 60%,#3c3936)"></div>
  <div class="abs h-display" style="left:635px;top:125px;font-size:40px;line-height:50px">Meet Paul Harnetti,</div>
  <div class="abs" style="left:635px;top:178px;font-size:15px;font-weight:500">Private Equity Investor</div>
  <div class="rule" style="left:635px;top:210px;height:2px"></div>
  <div class="abs body-text" style="left:635px;top:232px;width:420px">
    <p style="margin-bottom:10px">Paul Harnetti is a private equity investor providing significantly above market returns to his investment partners while taking the time to be involved with his community and family. Paul first honed his skills in taking calculated risk decisions while very young where he took on playing poker professionally.</p>
    <p>He succeeded at the highest levels for over a decade competing in high stakes professional cash games around the world.</p>
  </div>
  <div class="btn" style="left:635px;top:420px;width:127px">Read More</div>
</section>

<!-- Call to action -->
<section class="section" style="top:2870px;height:425px;background:linear-gradient(90deg,#8a6534,#a57d45 55%,#b38a4d)" role="img" aria-label="Warm-toned desert landscape with saguaro cactus and sun rays">
  <div class="abs center" style="top:85px;font-family:'Oswald',sans-serif;font-weight:600;font-size:49px;line-height:56px;color:var(--white);text-transform:uppercase">Get Started with<br>Ridgecrest Capital Allies</div>
  <p class="abs" style="left:250px;top:210px;width:700px;text-align:center;color:var(--white);font-size:16px;line-height:25px">Lorem Ipsum Dolor Sit Amet Consectetur Adipiscing Elit. Nunc Sit Amet Tortor Vel Enim Efficitur Vulputate Vel Nec Leo.</p>
  <div class="btn" style="left:537px;top:286px;width:126px;background:var(--white);color:var(--brown)">Contact Us</div>
</section>

<!-- Testimonials -->
<section class="section" style="top:3295px;height:545px"></section>
<div class="abs center h-display" style="top:3368px;font-size:40px;line-height:50px">What Our Partners Say</div>
<div class="rule" style="left:569px;top:3428px"></div>
<div class="card" style="left:141px"><div class="quote">&ldquo;</div><div class="stars">★★★★★</div><p>Lorem ipsum dolor sit amet, consectetur adipiscing elit. Nunc sit amet tortor vel enim efficitur vulputate vel leo. Donec accumsan venenatis leo dictum vestibulum.</p><div class="who">Dana R.</div></div>
<div class="card" style="left:615px"><div class="quote">&ldquo;</div><div class="stars">★★★★★</div><p>Lorem ipsum dolor sit amet, consectetur adipiscing elit. Nunc sit amet tortor vel enim efficitur vulputate vel leo. Donec accumsan venenatis leo dictum vestibulum.</p><div class="who">Mei T.</div></div>
<div class="arrow" style="left:85px;border:1.5px solid #cfcfcf"><svg width="16" height="16" viewBox="0 0 16 16" fill="none" stroke="#bbb" stroke-width="2"><path d="M14 8H2M7 3L2 8l5 5"/></svg></div>
<div class="arrow" style="left:1080px;background:var(--brown)"><svg width="16" height="16" viewBox="0 0 16 16" fill="none" stroke="#fff" stroke-width="2"><path d="M2 8h12M9 3l5 5-5 5"/></svg></div>
<div class="btn" style="left:537px;top:3716px;width:126px">Contact Us</div>

<!-- Contact -->
<section class="section" style="top:3840px;height:540px;background:var(--cream)">
  <div class="abs center h-display" style="top:73px;font-size:40px;line-height:50px">Contact Us</div>
  <div class="rule" style="left:569px;top:133px"></div>
  <div class="field-label" style="left:281px;top:157px">First Name*</div>
  <div class="field field-active" style="left:281px;top:173px;width:310px">John |</div>
  <div class="field" style="left:609px;top:173px;width:309px">Latest Name*</div>
  <div class="field" style="left:281px;top:235px;width:310px">Email*</div>
  <div class="field" style="left:609px;top:235px;width:309px">Phone*</div>
  <div class="field" style="left:281px;top:295px;width:637px;height:92px">Message</div>
  <div class="abs" style="left:281px;top:410px;width:637px;height:46px;background:var(--brown);color:var(--white);font-size:12.5px;display:flex;align-items:center;justify-content:center">Submit Now</div>
</section>

<!-- Footer -->
<footer class="section footer">
  <div class="logo" style="left:458px;top:45px">
    <div class="logo-mark" style="width:88px;height:88px"></div>
    <div class="logo-text"><div class="logo-name" style="color:var(--white)">Ridgecrest</div><div class="logo-tag" style="color:var(--white)">Capital Allies</div></div>
  </div>
  <div class="abs" style="left:141px;top:188px;width:918px;height:1px;background:rgba(255,255,255,0.2)"></div>
  <div class="foot-item" style="left:141px;top:240px"><div class="foot-icon"><svg width="14" height="16" viewBox="0 0 14 16" fill="#fff"><path d="M7 0a6 6 0 0 1 6 6c0 4-6 10-6 10S1 10 1 6a6 6 0 0 1 6-6zm0 3.5A2.5 2.5 0 1 0 7 8.5 2.5 2.5 0 0 0 7 3.5z"/></svg></div><div>123, Building Name, Street<br>City, State XY 123456</div></div>
  <div class="foot-item" style="left:540px;top:240px"><div class="foot-icon"><svg width="16" height="16" viewBox="0 0 16 16" fill="#fff"><path d="M3 1l3 3-2 2c1 2 3 4 6 6l2-2 3 3-2 2C7 15 1 9 1 3z"/></svg></div><div><div class="foot-label">PHONE</div>123 456 7890</div></div>
  <div class="foot-item" style="left:816px;top:240px"><div class="foot-icon"><svg width="16" height="12" viewBox="0 0 16 12" fill="none" stroke="#fff" stroke-width="1.5"><rect x="1" y="1" width="14" height="10"/><path d="M1 1l7 6 7-6"/></svg></div><div><div class="foot-label">EMAIL</div>Paul@RidgecrestFunds.example</div></div>
  <div class="bottom-bar"><span>© 2024 RIDGECREST Capital Allies. All Rights Reserved.</span><div class="socials"><div class="social"></div><div class="social"></div></div></div>
</footer>

</body>
</html>
```